New boutique IT consultancy needs business card

I need a business card and logo for my IT consultancy business, called 'Quenbrylle' . I want it to make me look bigger than I am. I want it to look classy, and modern. Simple design, that will be easy for me to translate into my webpage etc. The business card should be bold, and different.

The logo should emphasise the 'y' as used in quenbrylle

Target Market(s)

IT divisions in other companies

Industry/Entity Type

Business

Contact Information for Business Card

Marcel Thornby
Director
+61 437 819 063
mthornby@quenbrylle-mail.com

```html
<!DOCTYPE html>
<html lang="en">
<head>
<meta charset="utf-8">
<title>Quenbrylle business card</title>
<link rel="stylesheet" href="https://fonts.googleapis.com/css2?family=Open+Sans:wght@400;600&family=Raleway:wght@400&display=swap">
<style>
  :root {
    --canvas-bg: #eeeeec;
    --card-white: #ffffff;
    --brand-green: #8ae41d;
    --brand-blue: #0077c8;
    --ink: #3a3a3a;
    --ink-soft: #444444;
  }
  * { box-sizing: border-box; margin: 0; padding: 0; }
  html, body {
    width: 1200px;
    height: 900px;
    overflow: hidden;
    background: var(--canvas-bg);
  }
  .canvas {
    position: relative;
    width: 1200px;
    height: 900px;
  }
  .card {
    position: absolute;
    width: 556px;
    height: 343px;
    background: var(--card-white);
    box-shadow: 0 6px 18px rgba(0, 0, 0, 0.12);
    overflow: hidden;
  }
  .card--front { left: 238px; top: 62px; }
  .card--back { left: 457px; top: 518px; width: 560px; }

  /* front: colour bands */
  .band { position: absolute; top: 0; height: 100%; }
  .band--info { left: 0; width: 268px; background: var(--brand-green); }
  .band--blue { left: 276px; width: 108px; background: var(--brand-blue); }
  .band--green { left: 390px; right: 0; background: var(--brand-green); }

  .info { position: absolute; left: 35px; top: 0; width: 222px; color: var(--ink); }
  .wordmark {
    font-family: "Raleway", sans-serif;
    font-weight: 400;
    color: var(--ink);
    line-height: 1;
    text-transform: uppercase;
    white-space: nowrap;
  }
  .info .wordmark { position: absolute; top: 80px; font-size: 31px; letter-spacing: 0; }
  .person { position: absolute; top: 150px; font-family: "Open Sans", sans-serif; }
  .person__name { font-size: 17px; font-weight: 600; color: var(--ink); line-height: 22px; }
  .person__role { font-size: 13.5px; font-weight: 400; color: var(--ink-soft); line-height: 18px; }

  .contacts {
    position: absolute;
    top: 217px;
    list-style: none;
    font-family: "Open Sans", sans-serif;
    font-size: 13px;
    letter-spacing: -0.2px;
    color: var(--ink-soft);
  }
  .contacts li { display: flex; align-items: center; height: 20px; white-space: nowrap; }
  .contacts svg { width: 11px; height: 11px; margin-right: 10px; fill: var(--ink); flex: none; }

  /* back */
  .card--back .wordmark {
    position: absolute;
    left: 0;
    right: 0;
    top: 197px;
    text-align: center;
    font-size: 50px;
    letter-spacing: 0.5px;
  }
</style>
</head>
<body>
<main class="canvas">

  <section class="card card--front" aria-label="Business card front">
    <div class="band band--info"></div>
    <div class="band band--blue"></div>
    <div class="band band--green"></div>

    <div class="info">
      <p class="wordmark">Quenbrylle</p>
      <div class="person">
        <p class="person__name">Marcel Thornby</p>
        <p class="person__role">Director</p>
      </div>
      <ul class="contacts">
        <li>
          <svg viewBox="0 0 12 12" aria-hidden="true"><path d="M2.6 0.6 4.4 2.8 3.4 4.2C4 5.6 6.2 7.8 7.8 8.6L9.2 7.6 11.4 9.4 10.2 11.4C5.6 11.4 0.6 6.4 0.6 1.8Z"/></svg>
          +61 437 819 063
        </li>
        <li>
          <svg viewBox="0 0 12 12" aria-hidden="true"><path d="M1 2.5H11V9.5H1ZM1.8 3.2 6 6.4 10.2 3.2V3.2H1.8Z"/></svg>
          mthornby@quenbrylle-mail.com
        </li>
        <li>
          <svg viewBox="0 0 12 12" aria-hidden="true"><circle cx="6" cy="6" r="5.5"/></svg>
          www.quenbrylle.com
        </li>
      </ul>
    </div>
  </section>

  <section class="card card--back" aria-label="Business card back">
    <p class="wordmark">Quenbrylle</p>
  </section>

</main>
</body>
</html>
```